Business Card Design - Local Discount Club

Looking for a fun business card for a local discount club. One side should be the logo only and the other should be have :

Name
Title
Phone, Email
Website

```html
<!DOCTYPE html>
<html lang="en">
<head>
<meta charset="utf-8">
<title>Harbor Perks Club – Business Card</title>
<link href="https://fonts.googleapis.com/css2?family=Montserrat:wght@700&family=Lato:wght@400;700&display=swap" rel="stylesheet">
<style>
  :root{
    --brand-blue:#3a5bbd;
    --sky-cyan:#4de1fb;
    --lime:#a8fc8e;
    --paper:#ffffff;
    --backdrop:#1a1a1a;
  }
  *{box-sizing:border-box;margin:0;padding:0}
  html,body{width:1200px;height:1122px;overflow:hidden;background:var(--backdrop)}
  .sheet{position:relative;width:1200px;height:1122px}
  .card{position:absolute;left:150px;width:900px;height:514px;border-radius:38px;overflow:hidden}
  .card--front{top:30px;background:var(--brand-blue);display:flex;align-items:center;justify-content:center}
  .card--back{top:578px;background:var(--paper)}
  .brand{display:flex;align-items:center;gap:22px;font-family:"Montserrat",sans-serif;font-weight:700;text-transform:uppercase;letter-spacing:1px}
  .brand__dot{width:38px;height:38px;border-radius:50%;flex:none}
  .brand__text{white-space:nowrap}
  .brand--front{color:var(--paper);font-size:56px}
  .brand--front .brand__dot{background:var(--sky-cyan)}
  .brand--back{position:absolute;left:540px;top:196px;color:var(--brand-blue);font-size:28px;gap:14px;line-height:1.15}
  .brand--back .brand__dot{width:26px;height:26px;background:var(--lime)}
  .bubble{position:absolute;border-radius:50%}
  .bubble--cyan{width:310px;height:310px;left:-30px;top:-135px;background:var(--sky-cyan)}
  .bubble--lime{width:210px;height:210px;left:300px;top:-50px;background:var(--lime)}
  .bubble--blue{width:830px;height:830px;left:-170px;top:150px;background:var(--brand-blue)}
  .contact{position:absolute;left:90px;top:282px;font-family:"Lato",sans-serif;color:var(--paper)}
  .contact__name{font-family:"Montserrat",sans-serif;font-weight:700;font-size:38px;letter-spacing:.5px;text-transform:uppercase}
  .contact__title{font-size:26px;color:var(--sky-cyan);margin-top:2px}
  .contact__list{list-style:none;margin-top:26px}
  .contact__item{display:flex;align-items:center;gap:16px;font-size:25px;margin-bottom:10px}
  .contact__icon{width:22px;height:22px;flex:none;color:var(--sky-cyan)}
</style>
</head>
<body>
<main class="sheet">
  <section class="card card--front" aria-label="Card front">
    <div class="brand brand--front"><span class="brand__dot"></span><span class="brand__text">Harbor Perks Club</span></div>
  </section>

  <section class="card card--back" aria-label="Card back">
    <span class="bubble bubble--cyan"></span>
    <span class="bubble bubble--lime"></span>
    <span class="bubble bubble--blue"></span>

    <div class="brand brand--back"><span class="brand__dot"></span><span class="brand__text">Harbor Perks<br>Club</span></div>

    <div class="contact">
      <h1 class="contact__name">Daniel Reyes</h1>
      <p class="contact__title">Founder &amp; CEO</p>
      <ul class="contact__list">
        <li class="contact__item">
          <svg class="contact__icon" viewBox="0 0 24 24" fill="currentColor" aria-hidden="true"><path d="M6.6 10.8a15.1 15.1 0 0 0 6.6 6.6l2.2-2.2a1 1 0 0 1 1-.25 11.4 11.4 0 0 0 3.6.57 1 1 0 0 1 1 1V20a1 1 0 0 1-1 1A17 17 0 0 1 3 4a1 1 0 0 1 1-1h3.5a1 1 0 0 1 1 1c0 1.25.2 2.45.57 3.57a1 1 0 0 1-.25 1z"/></svg>
          (555) 012-3480
        </li>
        <li class="contact__item">
          <svg class="contact__icon" viewBox="0 0 24 24" fill="currentColor" aria-hidden="true"><path d="M2 5h20v14H2zm2 2v.5l8 5 8-5V7zm0 2.8V17h16V9.8l-8 5z"/></svg>
          hello@harborperks.example
        </li>
        <li class="contact__item">
          <svg class="contact__icon" viewBox="0 0 24 24" fill="none" stroke="currentColor" stroke-width="2" aria-hidden="true"><circle cx="12" cy="12" r="9.5"/><path d="M2.5 12h19M12 2.5c3 3 3 16 0 19M12 2.5c-3 3-3 16 0 19"/></svg>
          harborperks.example
        </li>
      </ul>
    </div>
  </section>
</main>
</body>
</html>
```